KBR, LLC Original

I need a business card design for a new company in Gaithersburg, MD. Though the name of the company is Wiring By Candor (KBR) we specialize in commercial kitchen ventilation systems as a complete turnkey project or as a service provider. We can design the entire system including the hoods, fans, ductwork, and fire system. We also specialize in fire alarm service, design, install and inspection. We are experts on any Pellmoor Units equipment including Vexa PCU, Vexa Hoods, EMS controls, Standard controls, PCU filtration and Make-up Air units with heaters and cooling. We can repair/retrofit old water wash hood systems as well. We are experts with local code requirements and upgrades.

Industry/Entity Type

Business

Contact Information for Business Card

Neil Radcott, Wiring By Candor, LLC; 240-555-0182 Cell, Hollisbrook, MD 20874. Neilr@wiringbycandorco.example

```html
<!DOCTYPE html>
<html lang="en">
<head>
<meta charset="utf-8">
<title>Wiring By Candor — Business Card</title>
<link rel="stylesheet" href="https://fonts.googleapis.com/css2?family=Cinzel:wght@600&family=Arimo:wght@400;700&display=swap">
<style>
  :root {
    --stage: #2f2f2f;
    --card-dark: #231f20;
    --card-light: #ffffff;
    --ink-dark: #1a1718;
    --ink-light: #ffffff;
    --gloss: #3d3739;
  }
  * { margin: 0; padding: 0; box-sizing: border-box; }
  html, body { width: 1200px; height: 750px; overflow: hidden; }
  body {
    background: var(--stage);
    position: relative;
    font-family: "Arimo", Arial, sans-serif;
  }
  .card {
    position: absolute;
    top: 218px;
    width: 492px;
    height: 283px;
    background: var(--card-dark);
    overflow: hidden;
  }
  .card--front { left: 92px; }
  .card--back { left: 620px; }

  .front-header {
    position: absolute;
    left: 0; top: 0;
    width: 100%;
    height: 141px;
    background: var(--card-light);
    display: flex;
    align-items: center;
    justify-content: center;
    padding-top: 12px;
  }
  .company-name {
    font-family: "Cinzel", "Times New Roman", serif;
    font-weight: 600;
    font-size: 20px;
    letter-spacing: 0.6px;
    color: var(--ink-dark);
  }
  .person-name {
    position: absolute;
    left: 34px;
    top: 164px;
    font-weight: 700;
    font-size: 15px;
    color: var(--ink-light);
    letter-spacing: 0.2px;
  }
  .name-rule {
    position: absolute;
    left: 34px;
    top: 184px;
    width: 423px;
    height: 1px;
    background: var(--ink-light);
  }
  .contact-list {
    position: absolute;
    left: 34px;
    top: 207px;
    list-style: none;
  }
  .contact-list li {
    display: flex;
    align-items: center;
    height: 16px;
    font-size: 11.5px;
    color: var(--ink-light);
  }
  .contact-list svg {
    width: 12px;
    height: 12px;
    margin-right: 9px;
    fill: var(--ink-light);
  }
  .front-web {
    position: absolute;
    right: 33px;
    top: 240px;
    font-size: 11.5px;
    color: var(--ink-light);
  }
  .back-web {
    position: absolute;
    left: 0; top: 225px;
    width: 100%;
    text-align: center;
    font-size: 14px;
    letter-spacing: 1px;
    color: var(--gloss);
  }
</style>
</head>
<body>
  <section class="card card--front">
    <div class="front-header">
      <h1 class="company-name">WIRING BY CANDOR (KBR)</h1>
    </div>
    <p class="person-name">NEIL RADCOTT</p>
    <div class="name-rule"></div>
    <ul class="contact-list">
      <li>
        <svg viewBox="0 0 12 12" aria-hidden="true"><path d="M6 1 L0.5 6 H2 V11 H5 V8 H7 V11 H10 V6 H11.5 Z"/></svg>
        Hollisbrook, MD 20874
      </li>
      <li>
        <svg viewBox="0 0 12 12" aria-hidden="true"><path d="M1 4 Q6 0 11 4 L10 5.5 L8 4.8 V4 Q6 3 4 4 V4.8 L2 5.5 Z M3 6 H9 L10.5 10.5 H1.5 Z"/></svg>
        240-555-0182
      </li>
      <li>
        <svg viewBox="0 0 12 12" aria-hidden="true"><path d="M0.5 2.5 H11.5 V9.5 H0.5 Z M1.5 3.5 L6 7 L10.5 3.5" stroke="#231f20" stroke-width="0.9"/></svg>
        neilr@wiringbycandorco.example
      </li>
    </ul>
    <p class="front-web">www.wiringbycandorco.example</p>
  </section>

  <section class="card card--back">
    <p class="back-web">www.wiringbycandorco.example</p>
  </section>
</body>
</html>
```